TriVex Business Card Design - double sided -plumbing local plumbing company

We have a Plumbing company where the design was create through Sketch Hive. We would now like a business card designed as well. We want it to be in the colour version of the logo.

Details below for the card.

Phone Number: 0438 615 247
Email: info@trivexplumbing.example.au
Website: https://trivexplumbing.example.au
We really want a sophisticated design that stand out from the other- informative and timeless.

Target Market(s)

local Canberra market

Industry/Entity Type

Plumbing, gas fitting, hot water

Contact Information for Business Card

Phone number, email, logo and "Supplying all your heating, cooling and hot water needs"

Requirements
Must have
• bust be colourful, must also be though about it being printed on a magnet. must Vex with the logo - I dont want the logo and information chucked onto a white canvas I would prefer it to be smooth and look purposeful

```html
<!DOCTYPE html>
<html lang="en">
<head>
<meta charset="utf-8">
<title>TriVex Plumbing – Business Card</title>
<link rel="stylesheet" href="https://fonts.googleapis.com/css2?family=Montserrat:wght@400;500;600;700;800&display=swap">
<style>
  :root {
    --stage: #3b3b3d;
    --brand-blue: #317ac0;
    --brand-blue-soft: #4a8ccc;
    --paper: #ffffff;
    --tint: #dfe9f5;
    --ink: #2a2a2a;
  }
  * { margin: 0; padding: 0; box-sizing: border-box; }
  html, body { width: 1200px; height: 689px; overflow: hidden; }
  body {
    background: var(--stage);
    font-family: "Montserrat", sans-serif;
    position: relative;
  }
  .card {
    position: absolute;
    top: 184px;
    width: 560px;
    height: 320px;
    border-radius: 22px;
    overflow: hidden;
    box-shadow: 0 14px 30px rgba(0,0,0,.45);
  }
  .card--front { left: 27px; background: var(--brand-blue); }
  .card--back { left: 613px; background: var(--paper); }

  .decor-circle { position: absolute; border-radius: 50%; }
  .card--front .decor-circle {
    width: 300px; height: 300px; left: 130px; top: 10px;
    background: var(--brand-blue-soft); opacity: .55;
  }
  .card--back .decor-circle {
    width: 330px; height: 330px; left: 290px; top: -20px;
    background: var(--tint);
  }

  .wordmark {
    position: absolute;
    font-weight: 800;
    letter-spacing: 2px;
    line-height: 1;
    text-transform: uppercase;
  }
  .card--front .wordmark {
    color: var(--paper);
    left: 0; right: 0; top: 112px;
    text-align: center;
    font-size: 44px;
  }
  .wordmark .wordmark__sub { display: block; font-size: .42em; letter-spacing: 10px; margin-top: 8px; }

  .tagline {
    position: absolute;
    left: 0; right: 0; top: 212px;
    text-align: center;
    color: var(--paper);
    font-size: 12px;
    font-weight: 600;
    letter-spacing: .6px;
  }

  .card--back .wordmark {
    color: var(--brand-blue);
    left: 36px; top: 40px;
    font-size: 36px;
  }

  .person { position: absolute; left: 36px; top: 130px; }
  .person__name { color: var(--brand-blue); font-weight: 800; font-size: 21px; letter-spacing: .5px; }
  .person__title { color: var(--ink); font-weight: 500; font-size: 12px; letter-spacing: 1px; margin-top: 3px; }

  .contacts { position: absolute; left: 36px; top: 190px; list-style: none; }
  .contacts li {
    display: flex; align-items: center; gap: 10px;
    color: var(--ink); font-size: 12.5px; font-weight: 500;
    height: 20px;
    white-space: nowrap;
  }
  .contacts .icon { width: 14px; height: 14px; fill: var(--brand-blue); flex: none; }
  .contacts .address { padding-left: 24px; }
</style>
</head>
<body>
  <section class="card card--front" aria-label="Card front">
    <div class="decor-circle"></div>
    <div class="wordmark">TriVex<span class="wordmark__sub">Plumbing</span></div>
    <p class="tagline">Supplying all your heating, cooling and hot water needs</p>
  </section>

  <section class="card card--back" aria-label="Card back">
    <div class="decor-circle"></div>
    <div class="wordmark">TriVex<span class="wordmark__sub">Plumbing</span></div>

    <div class="person">
      <div class="person__name">MARCUS ELLERY</div>
      <div class="person__title">MANAGING DIRECTOR</div>
    </div>

    <ul class="contacts">
      <li>
        <svg class="icon" viewBox="0 0 24 24"><path d="M6.6 10.8a15 15 0 0 0 6.6 6.6l2.2-2.2c.3-.3.7-.4 1-.2 1.1.4 2.3.6 3.6.6.6 0 1 .4 1 1V20c0 .6-.4 1-1 1A17 17 0 0 1 3 4c0-.6.4-1 1-1h3.5c.6 0 1 .4 1 1 0 1.2.2 2.4.6 3.6.1.3 0 .7-.2 1z"/></svg>
        0438 615 247
      </li>
      <li>
        <svg class="icon" viewBox="0 0 24 24"><path d="M2 5h20v14H2z M4 7v.5l8 5 8-5V7z" fill-rule="evenodd"/></svg>
        info@trivexplumbing.example.au
      </li>
      <li>
        <svg class="icon" viewBox="0 0 24 24"><path d="M12 2a10 10 0 1 0 0 20 10 10 0 0 0 0-20zm0 2c.9 1.2 1.6 2.6 2 4h-4c.4-1.4 1.1-2.8 2-4zM4.3 14a8 8 0 0 1 0-4h3.4a16 16 0 0 0 0 4zm.8 2h3c.3 1.3.8 2.5 1.4 3.6A8 8 0 0 1 5.1 16zm3-8h-3a8 8 0 0 1 4.4-3.6C8.9 5.5 8.4 6.7 8.1 8zM12 20c-.9-1.2-1.6-2.6-2-4h4c-.4 1.4-1.1 2.8-2 4zm2.3-6H9.7a14 14 0 0 1 0-4h4.6a14 14 0 0 1 0 4zm.2 5.6c.6-1.1 1.1-2.3 1.4-3.6h3a8 8 0 0 1-4.4 3.6zm1.8-5.6a16 16 0 0 0 0-4h3.4a8 8 0 0 1 0 4zm-.4-6c-.3-1.3-.8-2.5-1.4-3.6A8 8 0 0 1 18.9 8z"/></svg>
        trivexplumbing.example.au
      </li>
      <li class="address">14 Ridgeline Way, Kellmore</li>
      <li class="address">ACT 2698, Australia</li>
    </ul>
  </section>
</body>
</html>
```